Dietary supplement, Clean and simple.

Hi,
I’d like to talk about the project,

About us:
We are a dietary supplement (Vitamins, Minerals, amino acids etc.) company.
The goal is to have about 25 products at the end of this year. However, for this goal to be achieved we need a good label design to make our products represent our company values.
I’ll be here every day supporting your questions, we are fully committed to making the highest/best quality/customer experience possible.

About the design and our values:
- Professional (We are in the industry of professionalism and expertise. I would love to show we are competent at this, Id. Like to have the labels looks like we have done our research.)
- Efficient (White spacing, good use of the space available.)
- Simple (Straight forward, in 5 seconds they have to know what the product they have is/how functions. We’re trying to simplify it for the consumer.
- No distractions (the only visually “distracting” factor can be the vector art.)

The guidelines:
The goal is to have a universal design, with one element that changes (Vector art). I’ll attach a file/multiple files I think can show some visuals on what I’m looking for, and what parts of the design I think are good/bad.

Label size: 69x155mm (Front is 77.5mm)

Design whatever you think fits our image. You’re the design expert, all I care about is that it fits our company standards/image.

Use this color/font.
Font: Sans Serif
Main company color is Mind green #237D62 (Use this color for something in the design.)

What I thought would be cool/might looks ugly, who knows:
1. The front of the label: Should have 1 vector art, preferably in the top right corner. (That looks good in multiple colors. The vector can have multiple areas to color, I would prefer 2 main colors in the vector art. The interchangeable colors are used for multiple kinds of products.)
2. Text/product information on the left. The text that will have to be displayed:
- Product name for instance “Magnesium + B6”
- Description for the product for instance “Magnesium with ginger taste”
- Company name or logo. (Add ® behind it. We are soon to be trademark registered.)
3. We need to show the "daily intake" amount on the front and also the amount in the complete bottle. For instance, “Daily intake 1 capsule, 60 capsules”.
• You don’t have to design the backside of the label. After I chose a design, I’d like to chat and give specific information on what areas need to be assigned where. (Too complex because of the law.)
Updates

Hi, Please make the deadline 31 days total. I want designers to have the time to design. And not be rushed to finish it.

I want to extend the deadline because i feel like a slightly more medical look would be interesting. Hope you can come up with something!!

Target Market(s)

Dietary supplement consumers

Industry/Entity Type

Dietary supplements

Font styles to use
Sans Serif

Colors

Requirements
Must have
• Trademark icon "®" has to be at the top right after the company logo(text of logo)/name.

```html
<!DOCTYPE html>
<html lang="en">
<head>
<meta charset="utf-8">
<title>Calm Crest Vitamin D3 Label</title>
<link rel="stylesheet" href="https://fonts.googleapis.com/css2?family=IBM+Plex+Sans:wght@300;400;600;700&display=swap">
<style>
  :root {
    --band-grey: #bcbdbf;
    --paper: #ffffff;
    --ink: #231f20;
    --mind-green: #237d62;
    --blue-light: #3d74b9;
    --blue-dark: #2a2c6e;
  }
  html, body {
    margin: 0;
    padding: 0;
    width: 1200px;
    height: 1200px;
    overflow: hidden;
    background: var(--paper);
  }
  .label {
    display: block;
    width: 1200px;
    height: 1200px;
    font-family: "IBM Plex Sans", sans-serif;
  }
  .band { fill: var(--band-grey); }
  .brand-line { font-size: 52px; font-weight: 400; fill: var(--ink); letter-spacing: 1px; }
  .brand-line .reg { font-size: 26px; }
  .product-name { font-size: 88px; font-weight: 700; fill: var(--ink); }
  .product-desc { font-size: 52px; font-weight: 300; fill: var(--ink); letter-spacing: 1px; }
  .divider-dashed { stroke: var(--mind-green); stroke-width: 2.5; stroke-dasharray: 6 12; }
  .capsule-icon { fill: none; stroke: var(--mind-green); stroke-width: 2.5; }
  .info-strong { font-size: 29px; font-weight: 600; fill: var(--mind-green); }
  .info-light { font-size: 28px; font-weight: 300; fill: var(--ink); letter-spacing: 0.5px; }
  .company-name { font-size: 38px; font-weight: 700; fill: var(--mind-green); letter-spacing: 1px; }
  .intake-rule { stroke: var(--mind-green); stroke-width: 3; }
</style>
</head>
<body>
<svg class="label" viewBox="0 0 1200 1200" xmlns="http://www.w3.org/2000/svg">
  <defs>
    <linearGradient id="art-vertical" x1="0" y1="0" x2="0" y2="1">
      <stop offset="0" stop-color="#3d74b9"/>
      <stop offset="1" stop-color="#2a2c6e"/>
    </linearGradient>
    <linearGradient id="rule-horizontal" x1="0" y1="0" x2="1" y2="0">
      <stop offset="0" stop-color="#3d74b9"/>
      <stop offset="1" stop-color="#2a2c6e"/>
    </linearGradient>
  </defs>

  <rect class="band band-top" x="0" y="0" width="1200" height="66"/>
  <rect class="band band-bottom" x="0" y="1134" width="1200" height="66"/>

  <rect class="product-art" role="img" aria-label="Product vector artwork area" x="445" y="66" width="310" height="387" fill="url(#art-vertical)"/>

  <text class="brand-line" x="600" y="537" text-anchor="middle">CALM CREST <tspan class="reg" dy="-18">®</tspan></text>
  <text class="product-name" x="600" y="637" text-anchor="middle">Vitamin D3</text>
  <rect class="title-rule" x="445" y="701" width="310" height="8" fill="url(#rule-horizontal)"/>
  <text class="product-desc" x="600" y="776" text-anchor="middle">Vitamin D3 2000iu</text>

  <line class="divider-dashed" x1="231" y1="940" x2="969" y2="940"/>

  <g class="pack-count">
    <rect class="capsule-icon" x="232" y="979" width="39" height="78" rx="19.5"/>
    <text class="info-strong" x="290" y="1011">60</text>
    <text class="info-light" x="290" y="1043">SOFTGELS</text>
  </g>

  <text class="company-name" x="600" y="1030" text-anchor="middle">CALM CREST</text>

  <g class="daily-intake">
    <text class="info-light" x="947" y="1011" text-anchor="end">DAILY INTAKE</text>
    <text class="info-strong" x="947" y="1043" text-anchor="end">1 SOFTGEL</text>
    <line class="intake-rule" x1="967" y1="979" x2="967" y2="1056"/>
  </g>
</svg>
</body>
</html>
```